Business Card Design for venture capital-focused company

I have a logo (attached), and would like business cards designed using the attached logo. Audience is mainly financial executives; services included finance/ accounting/ dashboards/ etc. Open to different design ideas. Thanks for your consideration.

Target Market(s)

Financial Executives, Venture Capital, etc.

Industry/Entity Type

Venture Capital

Contact Information for Business Card

Harbor Ledger Insights LLC
418 N Wexley Street
Maple Crest, WI 60214

Font styles to use
Serif
Sans Serif

```html
<!DOCTYPE html>
<html lang="en">
<head>
<meta charset="utf-8">
<title>Harbor Ledger Insights – Business Cards</title>
<link rel="stylesheet" href="https://fonts.googleapis.com/css2?family=Roboto:wght@300;400;500&display=swap">
<style>
  :root {
    --backdrop: #e9e9e7;
    --card: #3a3a3c;
    --edge-blue: #1f5fd6;
    --brand-blue: #2a63c9;
    --text-light: #f2f2f2;
    --text-muted: #d6d6d6;
    --rule: #cfcfcf;
  }
  * { margin: 0; padding: 0; box-sizing: border-box; }
  html, body {
    width: 1200px; height: 801px; overflow: hidden;
    background: var(--backdrop);
    font-family: "Roboto", Arial, sans-serif;
  }
  .sheet {
    position: relative; width: 1200px; height: 801px;
    display: flex; align-items: center; justify-content: center; gap: 50px;
  }
  .card {
    position: relative; width: 540px; height: 309px;
    background: var(--card);
    border-bottom: 3px solid var(--edge-blue);
    border-left: 2px solid var(--edge-blue);
    box-shadow: 0 10px 24px rgba(0,0,0,.18);
    color: var(--text-light);
  }
  .brand {
    display: flex; align-items: center; gap: 10px;
    font-weight: 400; color: var(--text-light);
  }
  .brand-dot {
    width: 14px; height: 14px; border-radius: 50%;
    background: var(--brand-blue); flex: none;
  }
  .card--contact .brand {
    position: absolute; right: 34px; top: 44px;
    font-size: 19px; letter-spacing: .04em;
  }
  .card--contact .divider {
    position: absolute; left: 34px; right: 34px; top: 150px;
    height: 1px; background: var(--rule);
  }
  .person { position: absolute; left: 34px; top: 92px; }
  .person-name { font-size: 21px; font-weight: 500; color: var(--brand-blue); }
  .person-role { font-size: 14px; color: var(--text-muted); margin-top: 6px; }
  .contact-list {
    position: absolute; left: 34px; top: 172px; list-style: none;
    font-size: 14px; font-weight: 300; color: var(--text-light);
  }
  .contact-list li { display: flex; align-items: center; gap: 10px; margin-bottom: 9px; }
  .contact-list svg { width: 13px; height: 13px; flex: none; }
  .contact-list .icon-fill { fill: var(--brand-blue); }
  .contact-list .icon-line { fill: none; stroke: var(--brand-blue); stroke-width: 1.4; }
  .contact-list .accent { color: var(--brand-blue); }
  .address {
    position: absolute; right: 34px; top: 172px; text-align: right;
    font-size: 14px; font-weight: 300; line-height: 1.45; color: var(--text-light);
    font-style: normal;
  }
  .card--logo { display: flex; align-items: center; justify-content: center; }
  .card--logo .brand { font-size: 30px; letter-spacing: .05em; gap: 14px; }
  .card--logo .brand-dot { width: 20px; height: 20px; }
</style>
</head>
<body>
<main class="sheet">
  <section class="card card--contact" aria-label="Business card, contact side">
    <div class="brand"><span class="brand-dot"></span>Harbor Ledger Insights</div>
    <div class="person">
      <p class="person-name">Daniel Mercer</p>
      <p class="person-role">Manager</p>
    </div>
    <div class="divider"></div>
    <ul class="contact-list">
      <li><svg class="icon-fill" viewBox="0 0 16 16"><path d="M3.6 1.5l2.3 2.6-1.2 1.9a9 9 0 0 0 5.3 5.3l1.9-1.2 2.6 2.3-1.4 2.1C7.9 14.6 1.4 8.1 1.5 2.9z"/></svg><span>312-555-0147</span></li>
      <li><svg class="icon-fill" viewBox="0 0 16 16"><path d="M1 3h14v10H1zm1.5 1.5v.3L8 9l5.5-4.2v-.3zm0 2.2v4.8h11V6.7L8 10.9z"/></svg><span>daniel@harborledger.co</span></li>
      <li><svg class="icon-line" viewBox="0 0 16 16"><circle cx="8" cy="8" r="6.3"/><ellipse cx="8" cy="8" rx="2.8" ry="6.3"/><path d="M1.7 8h12.6"/></svg><span>www.<span class="accent">harborledger</span>.co</span></li>
    </ul>
    <address class="address">418 N Wexley Street<br>Maple Crest, WI 60214</address>
  </section>

  <section class="card card--logo" aria-label="Business card, brand side">
    <div class="brand"><span class="brand-dot"></span>Harbor Ledger Insights</div>
  </section>
</main>
</body>
</html>
```